Welcome Center Signage/logo Design with Multicultural Relevance

We are looking to have a welcome signage/logo designed for our church lobby with either the word "welcome" or "Welcome to the Maplecrest Fellowship Church!"

This design must include our organizational logo (attached). It could (but does not need to) also include our church vision: "Our vision is to be a thriving diverse urban church sharing Christ's love and serving the needs of our local and global communities." The logo/signage will be printed on 4' x 6' stretch fabric.

This signage will then be hung up behind our welcome center...it will be one of the first things people see upon entering our building.

We are an urban multicultural church that has significant outreach into our local community, one that is quite culturally diverse. If you would like more information about our church, please visit www.maplecrestfellow.org.
Updates

Project Deadline Extended
Reason: We have committed to continue work with the designers on designs submitted over the last several days, and are scheduling the additional time needed to do so. Thank you!

Target Market(s)

Culturally (African American, Hispanic American, Asian American, European American) diverse millennials and iGens

Industry/Entity Type

Church

Font styles to use
Sans Serif

Requirements
Must have
• Our logo
Nice to have
• "Welcome" in many languages
Should not have
• I can't think of anything at the moment.

```html
<!DOCTYPE html>
<html lang="en">
<head>
<meta charset="utf-8">
<title>Welcome – Maplecrest Fellowship Church</title>
<link href="https://fonts.googleapis.com/css2?family=Figtree:wght@500;600&display=swap" rel="stylesheet">
<style>
  :root {
    --band-grey: #7d7c74;
    --band-navy: #132b46;
    --text-grey: #7d7c74;
    --mark-plum: #4a2a3c;
    --mark-ring: #c8202e;
  }
  * { margin: 0; padding: 0; box-sizing: border-box; }
  html, body { width: 1200px; height: 838px; overflow: hidden; background: #ffffff; }
  .sign {
    position: relative;
    width: 1200px;
    height: 838px;
    font-family: "Figtree", "Avenir Next", sans-serif;
    font-weight: 600;
  }
  .sign__header {
    position: absolute; left: 0; top: 0;
    width: 1200px; height: 447px;
    background: var(--band-grey);
  }
  .church-mark {
    position: absolute;
    left: 490px; top: 58px;
    width: 220px; height: 220px;
    border-radius: 50%;
    background: var(--mark-plum);
    border: 6px solid var(--mark-ring);
  }
  .church-name {
    position: absolute;
    left: 0; top: 318px;
    width: 1200px;
    text-align: center;
    font-size: 44px;
    line-height: 1;
    color: var(--band-navy);
  }
  .sign__greetings {
    position: absolute; left: 0; top: 447px;
    width: 1200px; height: 391px;
    background: var(--band-navy);
    color: var(--text-grey);
  }
  .greeting {
    position: absolute;
    font-size: 68px;
    line-height: 1;
    white-space: nowrap;
  }
  .greeting--english { left: 0; width: 1200px; text-align: center; top: 22px; }
  .greeting--spanish { left: 59px; top: 148px; }
  .greeting--swedish { right: 48px; top: 148px; }
  .greeting--german  { left: 0; width: 1200px; text-align: center; top: 258px; }
</style>
</head>
<body>
  <main class="sign">
    <header class="sign__header">
      <div class="church-mark" aria-hidden="true"></div>
      <p class="church-name">Maplecrest Fellowship Church</p>
    </header>
    <section class="sign__greetings">
      <p class="greeting greeting--english" lang="en">Welcome!</p>
      <p class="greeting greeting--spanish" lang="es">Bienvenido!</p>
      <p class="greeting greeting--swedish" lang="sv">Välkommen!</p>
      <p class="greeting greeting--german" lang="de">Herzlich willkommen!</p>
    </section>
  </main>
</body>
</html>
```